Zielgruppe
Dogwalking, Gassi- Service in und um Aidlingen, Bedürfnisorienterer Umgang, positive Verstärkung, Auslastung in der Gruppe,
Zielgruppe sind alle Berufstätigen, Vielbeschäftigten, Familien, denen die Zeit fehlt ihren Hund artgerecht auszulasten
Aufgabenstellung
Es soll nicht textüberladen sein und ins Auge springen,
www.frohe-pfoetli.de
Gassi Service & Hundebetreuung
+Logo

```html
<!DOCTYPE html>
<html lang="de">
<head>
<meta charset="utf-8">
<title>Wedelglück – Fahrzeugbeschriftung</title>
<link rel="stylesheet" href="https://fonts.googleapis.com/css2?family=Open+Sans:ital,wght@0,600;1,700&family=Lobster&display=swap">
<style>
  :root {
    --canvas: #ffffff;
    --body-grey: #6e7272;
    --body-grey-dark: #575b5b;
    --glass: #7f8383;
    --teal: #52bfbf;
    --teal-deep: #0f605d;
    --teal-mid: #3aa9a8;
    --white: #ffffff;
    --photo-light: #e9c9a2;
    --photo-dark: #c79a6c;
  }
  html, body {
    margin: 0;
    padding: 0;
    width: 1200px;
    height: 1117px;
    overflow: hidden;
    background: var(--canvas);
  }
  .wrap-sheet { display: block; width: 1200px; height: 1117px; }
  .headline { font-family: "Open Sans", sans-serif; font-weight: 700; font-style: italic; fill: var(--white); }
  .contact { font-family: "Open Sans", sans-serif; font-weight: 700; font-style: italic; fill: var(--white); }
  .tagline { font-family: "Lobster", cursive; fill: var(--teal-deep); }
  .brand-name { font-family: "Open Sans", sans-serif; font-weight: 600; fill: var(--white); }
</style>
</head>
<body>
<svg class="wrap-sheet" viewBox="0 0 1200 1117" xmlns="http://www.w3.org/2000/svg">
  <defs>
    <clipPath id="side-outline">
      <path d="M97 250 Q110 190 200 175 L330 120 Q380 90 470 88 L1020 92 Q1052 95 1056 130 L1060 390 Q1060 420 1030 420 L125 420 Q97 420 97 392 Z"/>
    </clipPath>
    <linearGradient id="photo-tone" x1="0" y1="0" x2="0" y2="1">
      <stop offset="0" stop-color="var(--photo-light)"/>
      <stop offset="1" stop-color="var(--photo-dark)"/>
    </linearGradient>
  </defs>

  <!-- Side panel -->
  <g class="side-panel" clip-path="url(#side-outline)">
    <rect class="side-base" x="90" y="80" width="980" height="350" fill="var(--body-grey)"/>
    <path class="side-window" d="M370 118 L590 105 L592 215 L370 230 Z" fill="var(--glass)"/>
    <path class="side-window" d="M628 105 L800 103 L800 225 L628 225 Z" fill="var(--glass)"/>
    <path class="swoosh-deep" d="M790 88 L840 88 Q760 260 640 380 L620 380 Q730 250 790 88 Z" fill="var(--teal-deep)"/>
    <path class="swoosh-teal" d="M840 88 L1070 88 L1070 430 L630 430 L640 376 Q760 260 840 88 Z" fill="var(--teal)"/>
    <rect class="side-sill" x="90" y="372" width="980" height="60" fill="var(--body-grey-dark)" opacity="0.55"/>
  </g>

  <rect class="dog-photo" x="818" y="110" width="208" height="132" rx="40" fill="url(#photo-tone)"
        role="img" aria-label="Foto eines hellen Hundes mit großen Ohren, der über eine Kante schaut"/>

  <g class="question-box">
    <rect x="783" y="228" width="90" height="24" fill="var(--white)"/>
    <text class="tagline" x="828" y="248" font-size="20" text-anchor="middle">Keine Zeit</text>
    <rect x="766" y="258" width="172" height="24" fill="var(--white)"/>
    <text class="tagline" x="852" y="278" font-size="20" text-anchor="middle">für Deinen Liebling?</text>
  </g>

  <text class="headline" x="731" y="314" font-size="23">Dogwalking/Gassi-Service</text>
  <g class="contact" font-size="12">
    <text x="727" y="335">Lena Marbach</text>
    <text x="708" y="349">0123/98765432</text>
    <text x="683" y="363">gassirunde-web.de</text>
  </g>

  <g class="brand side-brand">
    <circle cx="498" cy="300" r="30" fill="none" stroke="var(--white)" stroke-width="3"/>
    <text class="brand-name" x="498" y="357" font-size="26" text-anchor="middle">Wedelglück</text>
  </g>

  <!-- Rear panel -->
  <g class="rear-panel">
    <path class="rear-body" d="M418 585 L820 585 Q836 590 838 620 L842 945 Q842 962 825 962 L413 962 Q398 962 398 945 L402 620 Q404 590 418 585 Z" fill="var(--teal)"/>
    <rect class="rear-window" x="445" y="612" width="353" height="150" rx="22" fill="var(--glass)"/>
    <rect class="rear-band" x="398" y="870" width="444" height="40" fill="var(--teal-mid)" opacity="0.5"/>
    <rect class="rear-bumper" x="398" y="940" width="444" height="26" rx="6" fill="var(--body-grey-dark)"/>
  </g>

  <g class="headline" font-size="25">
    <text x="451" y="790">Dogwalking</text>
    <text x="451" y="816">Gassi-Service</text>
  </g>
  <g class="contact" font-size="12.5">
    <text x="451" y="836">Lena Marbach</text>
    <text x="451" y="850">0123/98765432</text>
    <text x="451" y="864">gassirunde-web.de</text>
  </g>

  <g class="brand rear-brand">
    <circle cx="745" cy="800" r="24" fill="none" stroke="var(--white)" stroke-width="3"/>
    <text class="brand-name" x="745" y="850" font-size="22" text-anchor="middle">Wedelglück</text>
  </g>
</svg>
</body>
</html>
```